Simple, Professional and neat business card design for Vendralo Inc.

We're looking to re-vamp our business card design. We're a supplier of innovative feed ingredients for the North American animal agriculture industry. We are located in Lucknow, Ontario, Canada and our flagship product is a product that prevents milk fever in dairy cows when the calve, it is fed before calving and is very effective compared to other alternatives available on the market today.

Our company has Danish roots and we import all of our product from our Danish partner/manufacturer in Denmark. We like our design to embrace high professionalism while remaining neat and simple.

Target Market(s)

B2B, Feed Mills, Veterinary Clinics, Large integrators/producers,

Industry/Entity Type

Agribusiness

Contact Information for Business Card

We like the rounded corners because they make the card easy to sit in a wallet and not many use it so it makes the card stand out, just possibly something to take account for during the design.

As you can also see on the sliders below, looking for a that simple but proffesional scandinavian design.

Requirements
Nice to have
• Rounded corners
Should not have
• Too vibrant

```html
<!DOCTYPE html>
<html lang="en">
<head>
<meta charset="utf-8">
<title>Vendralo Inc. – Business Card</title>
<link href="https://fonts.googleapis.com/css2?family=Barlow:wght@400;500&family=Rubik:wght@500;700&display=swap" rel="stylesheet">
<style>
  :root {
    --brand-blue: #0557a6;
    --ink: #1d1d1f;
    --paper: #ffffff;
    --backdrop: #e4e6e9;
    --rule: #2a2a2a;
  }
  * { box-sizing: border-box; margin: 0; padding: 0; }
  html, body { width: 1200px; height: 1200px; overflow: hidden; }
  body {
    background: var(--backdrop);
    display: flex;
    align-items: center;
    justify-content: center;
    gap: 70px;
    font-family: "Barlow", Arial, sans-serif;
  }
  .card {
    width: 460px;
    height: 805px;
    border-radius: 30px;
    box-shadow: 0 10px 30px rgba(0,0,0,0.12);
    display: flex;
    flex-direction: column;
    align-items: center;
  }

  /* Front */
  .card-front {
    background: var(--brand-blue);
    color: var(--paper);
    justify-content: space-between;
    padding: 230px 0 70px;
  }
  .front-brand { display: flex; flex-direction: column; align-items: center; gap: 36px; }
  .brand-circle {
    width: 150px; height: 150px; border-radius: 50%;
    border: 5px solid var(--paper);
  }
  .front-wordmark {
    font-family: "Rubik", Arial, sans-serif;
    font-weight: 700;
    font-size: 40px;
    letter-spacing: 0.5px;
  }
  .social-row { display: flex; align-items: center; gap: 10px; }
  .social-row .line { width: 70px; height: 2px; background: var(--paper); margin: 0 12px; }
  .social-dot { width: 30px; height: 30px; border-radius: 50%; background: var(--paper); }

  /* Back */
  .card-back {
    background: var(--paper);
    color: var(--ink);
    padding: 70px 55px 55px;
    text-align: center;
  }
  .back-brand { display: flex; flex-direction: column; align-items: center; gap: 18px; }
  .back-brand .brand-circle { width: 120px; height: 120px; border-color: var(--brand-blue); }
  .back-wordmark {
    font-family: "Rubik", Arial, sans-serif;
    font-weight: 700; font-size: 20px; color: var(--brand-blue); letter-spacing: 1px;
  }
  .person-name {
    margin-top: 40px;
    font-family: "Rubik", Arial, sans-serif;
    font-weight: 700; font-size: 31px; color: var(--brand-blue); line-height: 1;
  }
  .person-title { font-size: 22px; letter-spacing: 1px; margin-top: 4px; }
  .divider {
    display: flex; align-items: center; width: 100%; gap: 12px;
    margin: 16px 0 12px;
  }
  .divider .line { flex: 1; height: 2px; background: var(--rule); }
  .divider svg { width: 36px; height: 36px; flex: none; }
  .contact-lines { font-size: 21px; line-height: 1.2; }
  .contact-lines .label { font-size: 17px; }
  .website {
    margin-top: auto;
    font-family: "Rubik", Arial, sans-serif;
    font-weight: 700; font-size: 22px; color: var(--brand-blue);
  }
</style>
</head>
<body>

  <section class="card card-front">
    <div class="front-brand">
      <div class="brand-circle"></div>
      <div class="front-wordmark">VENDRALO INC.</div>
    </div>
    <div class="social-row" aria-label="Social media links">
      <span class="line"></span>
      <span class="social-dot"></span>
      <span class="social-dot"></span>
      <span class="social-dot"></span>
      <span class="line"></span>
    </div>
  </section>

  <section class="card card-back">
    <div class="back-brand">
      <div class="brand-circle"></div>
      <div class="back-wordmark">VENDRALO INC.</div>
    </div>

    <h1 class="person-name">MADS HOLMGREN</h1>
    <div class="person-title">TITLE</div>

    <div class="divider">
      <span class="line"></span>
      <svg viewBox="0 0 36 36" aria-hidden="true">
        <circle cx="18" cy="18" r="16" fill="none" stroke="#1d1d1f" stroke-width="2"/>
        <path d="M13 11c1-1 2-1 3 0l1.5 2.5c.5 1 0 1.8-.8 2.3 1 2 2.5 3.5 4.5 4.5.5-.8 1.3-1.3 2.3-.8L26 21c1 1 1 2 0 3-1.5 1.5-3.5 1.5-6 0-3-2-5-4-7-7-1.5-2.5-1.5-4.5 0-6z" fill="#1d1d1f"/>
      </svg>
      <span class="line"></span>
    </div>
    <div class="contact-lines">
      <div><span class="label">mobile:</span> 519.555.0147</div>
      <div><span class="label">office:</span> 519.555.0182</div>
      <div><span class="label">toll free:</span> 888.555.0139</div>
      <div><span class="label">fax:</span> 519.555.0196</div>
    </div>

    <div class="divider">
      <span class="line"></span>
      <svg viewBox="0 0 36 36" aria-hidden="true">
        <circle cx="18" cy="18" r="16" fill="none" stroke="#1d1d1f" stroke-width="2"/>
        <rect x="10" y="12" width="16" height="12" rx="1" fill="#1d1d1f"/>
        <path d="M10.5 12.5 18 19l7.5-6.5" fill="none" stroke="#fff" stroke-width="1.5"/>
      </svg>
      <span class="line"></span>
    </div>
    <div class="contact-lines">mads@vendralo.com</div>

    <div class="divider">
      <span class="line"></span>
      <svg viewBox="0 0 36 36" aria-hidden="true">
        <circle cx="18" cy="18" r="16" fill="none" stroke="#1d1d1f" stroke-width="2"/>
        <path d="M18 8a6.5 6.5 0 0 0-6.5 6.5c0 5 6.5 12.5 6.5 12.5s6.5-7.5 6.5-12.5A6.5 6.5 0 0 0 18 8z" fill="#1d1d1f"/>
        <circle cx="18" cy="14.5" r="2.5" fill="#fff"/>
      </svg>
      <span class="line"></span>
    </div>
    <address class="contact-lines" style="font-style: normal;">
      Box 420, Fairhaven, ON<br>Canada N0X 1A0
    </address>

    <div class="website">www.VENDRALO.com</div>
  </section>

</body>
</html>
```